Doctors clinic requires stationary designed

We require various types of stationary to be design based on the logo (attached). We require the following:
- Letterhead (A4 Portrait)
- Business Card (must include UV spot on rear)
- With compliments slip (DL Landscape)
- Appointments card (Folded A6)

We are a young clinical practice which boasts a modern and sophisticated approach to medicine so we require something which feels fresh and modern. Please include colours represented in the logo (contrasting teal and grey). We are calling for creative minds to put forth their ideas and we will be actively providing feedback on all designs.

thank you

Clinic

```html
<!DOCTYPE html>
<html lang="en">
<head>
<meta charset="utf-8">
<title>Dr Clara Whitfield – Letterhead</title>
<link href="https://fonts.googleapis.com/css2?family=Raleway:wght@400;600&family=Tinos:ital,wght@0,400;0,700;1,400&display=swap" rel="stylesheet">
<style>
  :root {
    --teal: #1a8f85;
    --grey: #8a8c8e;
    --ink: #1c1c1c;
    --muted: #555555;
    --paper: #ffffff;
    --backdrop: #e4e4e4;
    --rule: #d6d6d6;
  }
  * { box-sizing: border-box; margin: 0; padding: 0; }
  html, body { width: 1200px; height: 909px; overflow: hidden; }
  body { background: var(--backdrop); position: relative; font-family: "Raleway", sans-serif; }

  .letterhead {
    position: absolute; left: 296px; top: 24px;
    width: 608px; height: 860px;
    background: var(--paper);
    box-shadow: 0 2px 10px rgba(0,0,0,0.12);
    overflow: hidden;
  }

  .brand { position: absolute; left: 64px; top: 62px; display: flex; align-items: center; gap: 10px; }
  .brand-dot { width: 34px; height: 34px; border-radius: 50%; border: 2px solid var(--teal); }
  .brand-name { color: var(--teal); font-weight: 600; font-size: 19px; letter-spacing: -0.3px; line-height: 1; }
  .brand-role { color: var(--teal); font-size: 10.5px; margin-top: 4px; letter-spacing: 0.2px; }
  .brand-role .joiner { color: var(--grey); }

  .letter {
    position: absolute; left: 64px; top: 170px; width: 474px;
    font-family: "Tinos", serif; font-size: 11.5px; line-height: 1.28; color: var(--ink);
  }
  .letter p { margin-bottom: 14px; text-align: justify; }

  .sign-off { position: absolute; left: 64px; top: 520px; font-family: "Tinos", serif; font-size: 11.5px; line-height: 1.28; color: var(--ink); }
  .signature { width: 110px; height: 44px; margin: 6px 0 4px; background: linear-gradient(90deg, #f1f1f1, #e6e6e6); border-radius: 4px; }

  .web-tab {
    position: absolute; right: 0; top: 560px; width: 34px; height: 190px;
    background: var(--teal); border-radius: 22px 0 0 0;
    display: flex; align-items: center; justify-content: center;
  }
  .web-tab span {
    transform: rotate(-90deg); white-space: nowrap;
    color: #fff; font-size: 10.5px; letter-spacing: 1.6px;
  }

  .footer-rule { position: absolute; left: 64px; right: 34px; top: 730px; border-top: 1px solid var(--rule); }

  .contacts { position: absolute; left: 64px; top: 748px; list-style: none; }
  .contacts li { display: flex; align-items: flex-start; gap: 10px; font-size: 8.5px; letter-spacing: 1.2px; color: var(--muted); margin-bottom: 6px; line-height: 1.45; }
  .contacts svg { width: 11px; height: 11px; flex: none; fill: var(--teal); margin-top: 1px; }
</style>
</head>
<body>
<main class="letterhead">
  <header class="brand">
    <div class="brand-dot"></div>
    <div>
      <div class="brand-name">Dr Clara Whitfield</div>
      <div class="brand-role">Obstetrician <span class="joiner">and</span> Gynaecologist</div>
    </div>
  </header>

  <section class="letter">
    <p>Gentlemen,</p>
    <p>Enclosed I have the honor to send you an article which I should be pleased if you would accept for the “Civic Review”. I am <i>desperately</i> pushed for money; and in the event of Mr. Delaney’s liking the “Landscape-Garden” I would take it as an especial favor if you would mail me the amount due for it, so as to reach me here by the 21st, on which day I shall need it. Can you possibly oblige me in this? If you accept the paper I presume you will allow me your usual sum, whatever that is for similar contributions—but I set no price—leaving all to your own liberality. The piece will make 8 of your pages and rather more.</p>
    <p>Will you be kind enough to put the best possible interpretation upon my behavior while in N-York? You must have conceived a <i>queer</i> idea of me—but the simple truth is that Fenwick would insist upon <i>the juleps</i>, and I knew not what I was either doing or saying. The Review of Hartley which I offered you was deficient in a 1/2 page of commencement, which I had written to supersede the old beginning, and which gave the article the character of a general and retrospective review. No wonder you did not take it—I would have been very much mortified if you had. I hope to see you at some future time, under better auspices.</p>
  </section>

  <div class="sign-off">
    <p>In the meantime I remain</p>
    <p>Yours very truly,</p>
    <div class="signature" role="img" aria-label="Handwritten signature"></div>
    <p>Edwin A. Marlowe</p>
  </div>

  <div class="footer-rule"></div>

  <ul class="contacts">
    <li>
      <svg viewBox="0 0 24 24"><path d="M6.6 10.8a15 15 0 0 0 6.6 6.6l2.2-2.2c.3-.3.7-.4 1-.2 1.1.4 2.3.6 3.6.6.6 0 1 .4 1 1V20c0 .6-.4 1-1 1A17 17 0 0 1 3 4c0-.6.4-1 1-1h3.5c.6 0 1 .4 1 1 0 1.3.2 2.5.6 3.6.1.3 0 .7-.2 1z"/></svg>
      <span>9300 5170</span>
    </li>
    <li>
      <svg viewBox="0 0 24 24"><path d="M6 3h12v5H6zM4 9h16a2 2 0 0 1 2 2v6h-4v4H6v-4H2v-6a2 2 0 0 1 2-2zm4 7v3h8v-3z"/></svg>
      <span>9300 5171</span>
    </li>
    <li>
      <svg viewBox="0 0 24 24"><path d="M3 5h18v14H3zm2 2v.5l7 4.5 7-4.5V7zm0 2.8V17h14V9.8l-7 4.5z"/></svg>
      <span>clara@drclarawhitfield.com.au</span>
    </li>
    <li>
      <svg viewBox="0 0 24 24"><path d="M12 2a7 7 0 0 1 7 7c0 5-7 13-7 13S5 14 5 9a7 7 0 0 1 7-7zm0 4.5A2.5 2.5 0 1 0 12 11.5 2.5 2.5 0 0 0 12 6.5z"/></svg>
      <span>Harbourside Private Hospital<br>Level 3 Wellness Wing (North)<br>Coral Ave, Harbourside</span>
    </li>
  </ul>

  <aside class="web-tab"><span>drclarawhitfield.com.au</span></aside>
</main>
</body>
</html>
```